Powerpoint design for spirits and cosmetics packaging company

We need a powerpoint template that will be used for company presentations, projects, award ceremonies etc... We are packaging in the wine and spirits sector as well as in the cosmetics sector. Our job is to package our customers' bottles in gift boxes, to carry out labeling, quality control, etc. We are based in Cognac.
We work for the big names in luxury: QDRT, Vellane Ostrow, Trelumo, Syvanne etc...
The template should be neat with at least 10 different slides.
Cover page, summary page, product description page (several), page including a schedule, price presentation page.

Target Market(s)

premium spirits and cosmetics

Industry/Entity Type

Spiritueux et cosmétique

Font styles to use
Sans Serif

Requirements
Must have
• My project must have the logo attached, the possibility to add / modify photos afterwards. Must have about ten different slides

```html
<!DOCTYPE html>
<html lang="en">
<head>
<meta charset="utf-8">
<title>Atelier Cervaux – Presentation Template Overview</title>
<link href="https://fonts.googleapis.com/css2?family=Poppins:ital,wght@0,300;0,400;0,600;0,700;1,400&display=swap" rel="stylesheet">
<style>
:root{
  --red:#d42129;
  --orange:#f59d34;
  --grey:#8a8a8a;
  --light:#e6e6e6;
  --ink:#3a3a3a;
  --stage:#d5d5d7;
  --white:#ffffff;
}
html,body{margin:0;padding:0;overflow:hidden}
body{width:1200px;height:850px;background:var(--stage);position:relative;font-family:'Poppins',sans-serif}
.slide{position:absolute;width:176px;height:99px;background:var(--white);box-shadow:0 1px 3px rgba(0,0,0,.18);display:block}
.c1{left:54px}.c2{left:267px}.c3{left:490px}.c4{left:717px}.c5{left:934px}
.r1{top:57px}.r2{top:190px}.r3{top:313px}.r4{top:435px}.r5{top:568px}.r6{top:710px}
.slide text{font-family:'Poppins',sans-serif}
.title{font-size:8px;font-weight:700;fill:var(--red);text-anchor:middle}
.title-l{font-size:8px;font-weight:700;fill:var(--red)}
.sub{font-size:3px;fill:var(--ink);text-anchor:middle}
.body{font-size:3px;fill:var(--ink)}
.body-c{font-size:3px;fill:var(--ink);text-anchor:middle}
.body-w{font-size:3px;fill:var(--white)}
.label{font-size:4px;font-weight:700;fill:var(--red)}
.label-c{font-size:4px;font-weight:700;fill:var(--red);text-anchor:middle}
.label-o{font-size:4px;font-weight:700;fill:var(--orange)}
.label-w{font-size:4px;font-weight:700;fill:var(--white)}
.num{font-size:7px;font-weight:700;fill:var(--red);text-anchor:middle}
.fill-red{fill:var(--red)}.fill-orange{fill:var(--orange)}.fill-grey{fill:var(--grey)}.fill-light{fill:var(--light)}.fill-white{fill:var(--white)}
.line-red{stroke:var(--red);fill:none}
.line-grey{stroke:#bdbdbd;fill:none;stroke-width:.5}
.icon{fill:none;stroke:var(--red);stroke-width:1.6}
.defs{position:absolute;width:0;height:0}
</style>
</head>
<body>

<svg class="defs" aria-hidden="true">
  <defs>
    <linearGradient id="amber" x1="0" y1="0" x2="1" y2="1">
      <stop offset="0" stop-color="#6e4a33"/><stop offset=".55" stop-color="#b86b2c"/><stop offset="1" stop-color="#3a2a22"/>
    </linearGradient>
    <linearGradient id="cellar" x1="0" y1="0" x2="1" y2="1">
      <stop offset="0" stop-color="#8c8c8c"/><stop offset=".6" stop-color="#b08563"/><stop offset="1" stop-color="#4a3a33"/>
    </linearGradient>
    <linearGradient id="portrait" x1="0" y1="0" x2="0" y2="1">
      <stop offset="0" stop-color="#c9a690"/><stop offset="1" stop-color="#7a5a4c"/>
    </linearGradient>
    <linearGradient id="redAmber" x1="0" y1="0" x2="0" y2="1">
      <stop offset="0" stop-color="#c07a55"/><stop offset="1" stop-color="#d42129"/>
    </linearGradient>
    <symbol id="foot" viewBox="0 0 337 190">
      <rect y="178" width="337" height="12" fill="#d42129"/>
      <rect x="16" y="175" width="32" height="10" fill="#fff"/>
      <rect x="18" y="177" width="5" height="5" fill="#d42129"/>
      <text x="25" y="181.5" font-size="2.4" font-weight="600" fill="#d42129" font-family="Poppins,sans-serif">ATELIER CERVAUX</text>
      <text x="320" y="185.5" font-size="2.6" fill="#fff" text-anchor="end" font-family="Poppins,sans-serif">PAGE | 05</text>
    </symbol>
  </defs>
</svg>

<!-- Row 1 -->
<svg class="slide c1 r1" viewBox="0 0 337 190">
  <rect width="337" height="104" fill="url(#amber)" role="img" aria-label="Photo: hands opening a cognac bottle"/>
  <rect y="104" width="337" height="86" class="fill-red"/>
  <rect x="10" y="10" width="104" height="30" class="fill-white"/>
  <rect x="16" y="16" width="18" height="18" class="fill-red"/>
  <text x="40" y="28" font-size="7" font-weight="600" fill="#d42129">ATELIER CERVAUX</text>
  <text x="16" y="124" font-size="12" font-weight="300" fill="#fff">PRESENTATION TITLE</text>
  <text x="16" y="142" font-size="8" font-weight="700" fill="#fff">SUBTITLE</text>
  <text x="16" y="181" class="body-w">JANUARY 2023</text>
  <text x="320" y="181" class="body-w" text-anchor="end">WWW.WEB.COM</text>
</svg>

<svg class="slide c2 r1" viewBox="0 0 337 190">
  <text x="168" y="26" class="title">Contents</text>
  <g class="body">
    <text x="50" y="52">Cover Slide</text><text x="128" y="52" text-anchor="end" font-weight="700">01</text>
    <text x="50" y="76">Contents</text><text x="128" y="76" text-anchor="end" font-weight="700">03</text>
    <text x="50" y="100">About Us</text><text x="128" y="100" text-anchor="end" font-weight="700">04</text>
    <text x="50" y="126">Our Mission</text><text x="128" y="126" text-anchor="end" font-weight="700">05</text>
    <text x="50" y="153">Our Vision</text><text x="128" y="153" text-anchor="end" font-weight="700">07</text>
    <text x="190" y="52">Infographic 1</text><text x="268" y="52" text-anchor="end" font-weight="700">01</text>
    <text x="190" y="76">Planning</text><text x="268" y="76" text-anchor="end" font-weight="700">03</text>
    <text x="190" y="100">Company info</text><text x="268" y="100" text-anchor="end" font-weight="700">04</text>
    <text x="190" y="126">Our Team</text><text x="268" y="126" text-anchor="end" font-weight="700">06</text>
    <text x="190" y="153">Dashboard</text><text x="268" y="153" text-anchor="end" font-weight="700">07</text>
  </g>
  <g stroke="#d42129" stroke-width=".6">
    <line x1="50" y1="55" x2="128" y2="55"/><line x1="50" y1="79" x2="128" y2="79"/><line x1="50" y1="103" x2="128" y2="103"/><line x1="50" y1="129" x2="128" y2="129"/><line x1="50" y1="156" x2="128" y2="156"/>
    <line x1="190" y1="55" x2="268" y2="55"/><line x1="190" y1="79" x2="268" y2="79"/><line x1="190" y1="103" x2="268" y2="103"/><line x1="190" y1="129" x2="268" y2="129"/><line x1="190" y1="156" x2="268" y2="156"/>
  </g>
  <use href="#foot"/>
</svg>

<svg class="slide c3 r1" viewBox="0 0 337 190">
  <text x="168" y="26" class="title">Our Vision</text>
  <rect x="18" y="52" width="319" height="60" class="fill-orange"/>
  <g font-size="4.4" font-style="italic" fill="#fff">
    <text x="36" y="66">Lorem ipsum dolor sit amet, consectetuer adipiscing elit, sed diam</text>
    <text x="36" y="79">nonummy nibh euismod tincidunt ut laoreet dolore magna aliquam erat</text>
    <text x="36" y="92">volutpat. Ut wisi enim ad minim veniam, quis nostrud exerci tation</text>
    <text x="36" y="105">ullamcorper suscipit lobortis nisl ut aliquip ex ea commodo consequat.</text>
  </g>
  <use href="#foot"/>
</svg>

<svg class="slide c4 r1" viewBox="0 0 337 190">
  <text x="168" y="26" class="title">Our Mission</text>
  <rect x="22" y="52" width="86" height="46" class="fill-light"/>
  <rect x="232" y="100" width="86" height="46" class="fill-light"/>
  <g>
    <text x="65" y="72" class="label-c">Mission 1</text>
    <text x="65" y="79" class="body-c">Lorem ipsum dolor sit amet</text><text x="65" y="84" class="body-c">consectetuer adipiscing elit</text><text x="65" y="89" class="body-c">sed diam nonummy nibh</text>
    <text x="65" y="122" class="label-c">Mission 1</text>
    <text x="65" y="129" class="body-c">Lorem ipsum dolor sit amet</text><text x="65" y="134" class="body-c">consectetuer adipiscing elit</text><text x="65" y="139" class="body-c">sed diam nonummy nibh</text>
    <text x="168" y="72" class="label-c" style="fill:var(--orange)">Mission 1</text>
    <text x="168" y="79" class="body-c">Lorem ipsum dolor sit amet</text><text x="168" y="84" class="body-c">consectetuer adipiscing elit</text><text x="168" y="89" class="body-c">sed diam nonummy nibh</text>
    <text x="168" y="122" class="label-c" style="fill:var(--orange)">Mission 1</text>
    <text x="168" y="129" class="body-c">Lorem ipsum dolor sit amet</text><text x="168" y="134" class="body-c">consectetuer adipiscing elit</text><text x="168" y="139" class="body-c">sed diam nonummy nibh</text>
    <text x="275" y="72" class="label-c">Mission 1</text>
    <text x="275" y="79" class="body-c">Lorem ipsum dolor sit amet</text><text x="275" y="84" class="body-c">consectetuer adipiscing elit</text><text x="275" y="89" class="body-c">sed diam nonummy nibh</text>
    <text x="275" y="122" class="label-c">Mission 1</text>
    <text x="275" y="129" class="body-c">Lorem ipsum dolor sit amet</text><text x="275" y="134" class="body-c">consectetuer adipiscing elit</text><text x="275" y="139" class="body-c">sed diam nonummy nibh</text>
  </g>
  <use href="#foot"/>
</svg>

<svg class="slide c5 r1" viewBox="0 0 337 190">
  <rect width="128" height="178" fill="url(#amber)" role="img" aria-label="Photo: gift-packed bottle neck with seal"/>
  <rect x="145" y="40" width="10" height="1" class="fill-red"/>
  <text x="145" y="52" class="title-l">Our Achievements</text>
  <text x="145" y="62" class="body">Lorem ipsum dolor sit amet, consectetuer adipiscing elit, sed diam nonummy</text>
  <text x="145" y="67" class="body">nibh euismod tincidunt ut laoreet dolore magna aliquam erat lorem ipsum</text>
  <text x="145" y="72" class="body">dolor sit amet, consectetuer adipiscing elit, sed diam nonummy nibh</text>
  <rect x="145" y="92" width="45" height="22" class="fill-light"/>
  <rect x="193" y="92" width="45" height="22" class="fill-light"/>
  <rect x="241" y="92" width="45" height="22" class="fill-orange"/>
  <text x="150" y="101" class="label">15</text><text x="150" y="109" class="body">Companies</text>
  <text x="198" y="101" class="label">1,000</text><text x="198" y="109" class="body">Clients</text>
  <text x="246" y="101" class="label-w">46</text><text x="246" y="109" class="body-w">Employees</text>
  <use href="#foot"/>
</svg>

<!-- Row 2 -->
<svg class="slide c1 r2" viewBox="0 0 337 190">
  <text x="168" y="26" class="title">Services</text>
  <text x="168" y="33" class="sub">Lorem ipsum dolor sit amet, consectetuer adipiscing elit,</text>
  <text x="168" y="38" class="sub">sed diam nonummy nibh euismod tincidunt ut laoreet</text>
  <rect x="17" y="50" width="83" height="70" fill="url(#cellar)" role="img" aria-label="Photo: bottle being labelled"/>
  <rect x="127" y="50" width="83" height="70" fill="url(#cellar)" role="img" aria-label="Photo: packaging workshop"/>
  <rect x="238" y="50" width="83" height="70" fill="url(#amber)" role="img" aria-label="Photo: bottle quality check"/>
  <text x="58" y="136" class="label-c">Service 1</text><text x="168" y="136" class="label-c">Service 2</text><text x="279" y="136" class="label-c">Service 3</text>
  <text x="58" y="143" class="body-c">Lorem ipsum dolor sit amet, consectetuer</text><text x="58" y="148" class="body-c">adipiscing elit, sed diam nonummy nibh</text>
  <text x="168" y="143" class="body-c">Lorem ipsum dolor sit amet, consectetuer</text><text x="168" y="148" class="body-c">adipiscing elit, sed diam nonummy nibh</text>
  <text x="279" y="143" class="body-c">Lorem ipsum dolor sit amet, consectetuer</text><text x="279" y="148" class="body-c">adipiscing elit, sed diam nonummy nibh</text>
  <use href="#foot"/>
</svg>

<svg class="slide c2 r2" viewBox="0 0 337 190">
  <text x="168" y="26" class="title">Our Company</text>
  <text x="168" y="33" class="sub">Lorem ipsum dolor sit amet, consectetuer adipiscing elit,</text>
  <text x="168" y="62" class="body-c">Lorem ipsum dolor sit amet, consectetuer adipiscing elit, sed diam nonummy nibh euismod tincidunt ut laoreet</text>
  <text x="168" y="68" class="body-c">dolore magna aliquam erat volutpat. Ut wisi enim ad minim veniam, quis nostrud exerci tation ullamcorper</text>
  <text x="168" y="74" class="body-c">lobortis nisl ut aliquip ex ea commodo consequat. Duis autem vel eum iriure dolor in hendrerit in vulputate</text>
  <text x="168" y="80" class="body-c">molestie consequat, vel illum dolore eu feugiat nulla facilisis at vero eros et accumsan et iusto odio</text>
  <text x="168" y="86" class="body-c">blandit praesent luptatum zzril delenit augue duis dolore te feugait nulla facilisi.</text>
  <rect x="192" y="132" width="50" height="24" class="fill-orange"/>
  <text x="34" y="141" class="label-c">2100</text><text x="34" y="148" class="body-c">Evaluations</text>
  <text x="112" y="141" class="label-c">3100</text><text x="112" y="148" class="body-c">Production profitably</text>
  <text x="217" y="141" class="label-c" style="fill:#fff">2100</text><text x="217" y="148" class="body-c" style="fill:#fff">Companies</text>
  <text x="300" y="141" class="label-c">14</text><text x="300" y="148" class="body-c">Certifications</text>
  <use href="#foot"/>
</svg>

<svg class="slide c3 r2" viewBox="0 0 337 190">
  <text x="168" y="26" class="title">Analysis Chart</text>
  <text x="18" y="56" class="label">Bar Chart</text>
  <line x1="32" y1="70" x2="32" y2="132" class="line-grey"/>
  <line x1="32" y1="132" x2="150" y2="132" class="line-grey"/>
  <g>
    <rect x="32" y="74" width="38" height="6" class="fill-red"/><rect x="70" y="74" width="25" height="6" class="fill-orange"/><rect x="95" y="74" width="45" height="6" class="fill-grey"/>
    <rect x="32" y="90" width="30" height="6" class="fill-red"/><rect x="62" y="90" width="28" height="6" class="fill-orange"/><rect x="90" y="90" width="20" height="6" class="fill-grey"/>
    <rect x="32" y="106" width="26" height="6" class="fill-red"/><rect x="58" y="106" width="34" height="6" class="fill-orange"/><rect x="92" y="106" width="18" height="6" class="fill-grey"/>
    <rect x="32" y="122" width="40" height="6" class="fill-red"/><rect x="72" y="122" width="22" height="6" class="fill-orange"/><rect x="94" y="122" width="16" height="6" class="fill-grey"/>
  </g>
  <text x="178" y="56" class="label">Analysis 1</text>
  <text x="178" y="63" class="body">Lorem ipsum dolor sit amet, consectetuer adipiscing elit, sed diam</text>
  <text x="178" y="68" class="body">nonummy nibh euismod tincidunt ut laoreet dolore magna aliquam</text>
  <text x="178" y="88" class="label">Analysis 2</text>
  <text x="178" y="95" class="body">Lorem ipsum dolor sit amet, consectetuer adipiscing elit, sed diam</text>
  <text x="178" y="100" class="body">nonummy nibh euismod tincidunt ut laoreet dolore magna aliquam</text>
  <text x="178" y="120" class="label">Analysis 3</text>
  <text x="178" y="127" class="body">Lorem ipsum dolor sit amet, consectetuer adipiscing elit, sed diam</text>
  <text x="178" y="132" class="body">nonummy nibh euismod tincidunt ut laoreet dolore magna aliquam</text>
  <use href="#foot"/>
</svg>

<svg class="slide c4 r2" viewBox="0 0 337 190">
  <text x="168" y="26" class="title">S.W.O.T Analysis</text>
  <text x="168" y="40" class="body-c">Lorem ipsum dolor sit amet, consectetuer adipiscing elit, sed diam nonummy nibh euismod</text>
  <text x="168" y="45" class="body-c">tincidunt ut laoreet dolore magna aliquam erat volutpat. Ut wisi enim ad minim veniam, quis</text>
  <rect x="86" y="78" width="80" height="100" class="fill-orange"/>
  <rect x="248" y="78" width="80" height="100" class="fill-orange"/>
  <text x="16" y="92" class="label">Strength</text>
  <text x="92" y="92" class="label-w">Weakness</text>
  <text x="172" y="92" class="label">Opportunity</text>
  <text x="254" y="92" class="label-w">Threat</text>
  <g class="body"><text x="16" y="100">1. Lorem ipsum dolor sit</text><text x="16" y="106">2. consectetuer adipiscing</text><text x="16" y="112">3. sed diam nonummy nibh</text><text x="16" y="118">4. euismod tincidunt ut</text></g>
  <g class="body-w"><text x="92" y="100">1. Lorem ipsum dolor sit</text><text x="92" y="106">2. consectetuer adipiscing</text><text x="92" y="112">3. sed diam nonummy nibh</text><text x="92" y="118">4. euismod tincidunt ut</text></g>
  <g class="body"><text x="172" y="100">1. Lorem ipsum dolor sit</text><text x="172" y="106">2. consectetuer adipiscing</text><text x="172" y="112">3. sed diam nonummy nibh</text><text x="172" y="118">4. euismod tincidunt ut</text></g>
  <g class="body-w"><text x="254" y="100">1. Lorem ipsum dolor sit</text><text x="254" y="106">2. consectetuer adipiscing</text><text x="254" y="112">3. sed diam nonummy nibh</text><text x="254" y="118">4. euismod tincidunt ut</text></g>
  <use href="#foot"/>
</svg>

<svg class="slide c5 r2" viewBox="0 0 337 190">
  <rect width="128" height="145" fill="url(#amber)" role="img" aria-label="Photo: rum bottle on a workbench"/>
  <text x="165" y="56" class="title-l" style="fill:var(--orange)">Process</text>
  <text x="165" y="66" class="body">Lorem ipsum dolor sit amet, consectetuer adipiscing elit, sed diam</text>
  <text x="165" y="71" class="body">nonummy nibh euismod tincidunt ut laoreet dolore magna aliquam</text>
  <g stroke="#d42129" stroke-width=".7" fill="none">
    <path d="M128 94 H163"/><path d="M128 112 H180"/><path d="M128 130 H198"/>
  </g>
  <g class="fill-red"><path d="M163 92 L167 94 L163 96Z"/><path d="M180 110 L184 112 L180 114Z"/><path d="M198 128 L202 130 L198 132Z"/></g>
  <text x="169" y="93" class="label">Step 1</text><text x="169" y="99" class="body">Lorem ipsum dolor sit amet, consectetuer adipiscing</text>
  <text x="186" y="111" class="label">Step 2</text><text x="186" y="117" class="body">Lorem ipsum dolor sit amet, consectetuer adipiscing</text>
  <text x="204" y="129" class="label">Step 3</text><text x="204" y="135" class="body">Lorem ipsum dolor sit amet, consectetuer adipiscing</text>
  <use href="#foot"/>
</svg>

<!-- Row 3 -->
<svg class="slide c1 r3" viewBox="0 0 337 190">
  <rect x="85" y="42" width="95" height="3" fill="#5aa63a"/>
  <rect y="45" width="180" height="128" fill="url(#amber)" role="img" aria-label="Photo: worker inspecting a bottle"/>
  <text x="182" y="56" class="title-l">Product</text>
  <text x="182" y="65" class="body">Lorem ipsum dolor sit amet, consectetuer adipiscing elit, sed diam</text>
  <text x="182" y="70" class="body">nonummy nibh euismod tincidunt ut laoreet dolore magna aliquam</text>
  <text x="182" y="82" class="label">Lorem ipsum do</text>
  <text x="182" y="88" class="body">Lorem ipsum dolor sit amet, consectetuer adipiscing elit</text>
  <text x="182" y="93" class="body">sed diam nonummy nibh euismod tincidunt ut laoreet</text>
  <text x="182" y="105" class="label">Lorem ipsum do</text>
  <text x="182" y="111" class="body">Lorem ipsum dolor sit amet, consectetuer adipiscing elit</text>
  <text x="182" y="116" class="body">sed diam nonummy nibh euismod tincidunt ut laoreet</text>
  <use href="#foot"/>
</svg>

<svg class="slide c2 r3" viewBox="0 0 337 190">
  <rect x="34" y="58" width="86" height="55" fill="url(#cellar)" role="img" aria-label="Photo: gloved hands with bottle"/>
  <rect x="160" y="56" width="86" height="55" fill="url(#cellar)" role="img" aria-label="Photo: bottle being packed"/>
  <rect x="120" y="113" width="86" height="55" fill="url(#cellar)" role="img" aria-label="Photo: packaging line"/>
  <text x="124" y="75" class="label">Item 2</text>
  <text x="124" y="81" class="body">Lorem ipsum dolor sit</text><text x="124" y="86" class="body">consectetuer adipiscing</text><text x="124" y="91" class="body">sed diam nonummy nibh</text>
  <text x="34" y="125" class="label">Item 1</text>
  <text x="34" y="131" class="body">Lorem ipsum dolor sit</text><text x="34" y="136" class="body">consectetuer adipiscing</text><text x="34" y="141" class="body">sed diam nonummy nibh</text>
  <text x="210" y="125" class="label">Item 3</text>
  <text x="210" y="131" class="body">Lorem ipsum dolor sit</text><text x="210" y="136" class="body">consectetuer adipiscing</text><text x="210" y="141" class="body">sed diam nonummy nibh</text>
  <text x="252" y="73" class="title-l">Images</text>
  <text x="252" y="82" class="body">Lorem ipsum dolor sit amet,</text><text x="252" y="87" class="body">consectetuer adipiscing elit</text><text x="252" y="92" class="body">sed diam nonummy nibh</text><text x="252" y="97" class="body">euismod tincidunt ut laoreet</text>
  <use href="#foot"/>
</svg>

<svg class="slide c3 r3" viewBox="0 0 337 190">
  <text x="168" y="26" class="title">Our Leaders</text>
  <text x="168" y="33" class="sub">Lorem ipsum dolor sit amet, consectetuer adipiscing elit.</text>
  <rect y="43" width="337" height="32" class="fill-orange"/>
  <g fill="url(#portrait)" stroke="#fff" stroke-width="2">
    <circle cx="50" cy="75" r="19" role="img" aria-label="Portrait photo of a team leader"/>
    <circle cx="130" cy="75" r="19" role="img" aria-label="Portrait photo of a team leader"/>
    <circle cx="213" cy="75" r="19" role="img" aria-label="Portrait photo of a team leader"/>
    <circle cx="290" cy="75" r="19" role="img" aria-label="Portrait photo of a team leader"/>
  </g>
  <g>
    <text x="50" y="105" class="label-c" style="font-size:3.4px">Noel Garret</text><text x="50" y="110" class="body-c">Manager</text>
    <text x="50" y="117" class="body-c">Lorem ipsum dolor sit amet,</text><text x="50" y="122" class="body-c">consectetuer adipiscing elit</text>
    <text x="130" y="105" class="label-c" style="font-size:3.4px">Noel Garret</text><text x="130" y="110" class="body-c">Manager</text>
    <text x="130" y="117" class="body-c">Lorem ipsum dolor sit amet,</text><text x="130" y="122" class="body-c">consectetuer adipiscing elit</text>
    <text x="213" y="105" class="label-c" style="font-size:3.4px">Noel Garret</text><text x="213" y="110" class="body-c">Manager</text>
    <text x="213" y="117" class="body-c">Lorem ipsum dolor sit amet,</text><text x="213" y="122" class="body-c">consectetuer adipiscing elit</text>
    <text x="290" y="105" class="label-c" style="font-size:3.4px">Noel Garret</text><text x="290" y="110" class="body-c">Manager</text>
    <text x="290" y="117" class="body-c">Lorem ipsum dolor sit amet,</text><text x="290" y="122" class="body-c">consectetuer adipiscing elit</text>
  </g>
  <use href="#foot"/>
</svg>

<svg class="slide c4 r3" viewBox="0 0 337 190">
  <text x="168" y="26" class="title">Our Team</text>
  <text x="168" y="33" class="sub">Lorem ipsum dolor sit amet, consectetuer adipiscing elit.</text>
  <rect x="270" y="38" width="67" height="70" rx="12" class="fill-orange"/>
  <g fill="url(#portrait)">
    <circle cx="57" cy="65" r="16" role="img" aria-label="Team member photo"/><circle cx="138" cy="65" r="16" role="img" aria-label="Team member photo"/><circle cx="221" cy="65" r="16" role="img" aria-label="Team member photo"/>
    <circle cx="297" cy="65" r="16" stroke="#fff" stroke-width="2" role="img" aria-label="Team member photo"/>
    <circle cx="57" cy="132" r="16" role="img" aria-label="Team member photo"/><circle cx="138" cy="132" r="16" role="img" aria-label="Team member photo"/><circle cx="221" cy="132" r="16" role="img" aria-label="Team member photo"/><circle cx="297" cy="132" r="16" role="img" aria-label="Team member photo"/>
  </g>
  <g>
    <text x="57" y="90" class="label-c" style="font-size:3px">Noel Garret</text><text x="57" y="95" class="body-c">Manager</text>
    <text x="138" y="90" class="label-c" style="font-size:3px">Noel Garret</text><text x="138" y="95" class="body-c">Manager</text>
    <text x="221" y="90" class="label-c" style="font-size:3px">Noel Garret</text><text x="221" y="95" class="body-c">Manager</text>
    <text x="297" y="90" class="label-c" style="font-size:3px;fill:#fff">Noel Garret</text><text x="297" y="95" class="body-c" style="fill:#fff">Manager</text>
    <text x="57" y="157" class="label-c" style="font-size:3px">Noel Garret</text><text x="57" y="162" class="body-c">Manager</text>
    <text x="138" y="157" class="label-c" style="font-size:3px">Noel Garret</text><text x="138" y="162" class="body-c">Manager</text>
    <text x="221" y="157" class="label-c" style="font-size:3px">Noel Garret</text><text x="221" y="162" class="body-c">Manager</text>
    <text x="297" y="157" class="label-c" style="font-size:3px">Noel Garret</text><text x="297" y="162" class="body-c">Manager</text>
  </g>
  <use href="#foot"/>
</svg>

<svg class="slide c5 r3" viewBox="0 0 337 190">
  <text x="168" y="26" class="title">Timeline</text>
  <line x1="22" y1="95" x2="315" y2="95" stroke="#999" stroke-width=".6" stroke-dasharray="2 1.5"/>
  <g>
    <circle cx="50" cy="95" r="6" class="fill-red"/><circle cx="93" cy="95" r="6" class="fill-orange"/><circle cx="136" cy="95" r="6" class="fill-red"/>
    <circle cx="179" cy="95" r="6" class="fill-orange"/><circle cx="222" cy="95" r="6" class="fill-red"/><circle cx="265" cy="95" r="6" class="fill-orange"/>
  </g>
  <g font-size="2.6" fill="#fff" text-anchor="middle" font-weight="600">
    <text x="50" y="96">2009</text><text x="93" y="96">2012</text><text x="136" y="96">2015</text><text x="179" y="96">2018</text><text x="222" y="96">2021</text><text x="265" y="96">2027</text>
  </g>
  <g>
    <text x="93" y="47" class="label-c" style="fill:var(--orange)">Item 1</text><text x="93" y="53" class="body-c">Lorem ipsum dolor sit amet,</text><text x="93" y="58" class="body-c">consectetuer adipiscing</text>
    <text x="179" y="47" class="label-c" style="fill:var(--orange)">Item 1</text><text x="179" y="53" class="body-c">Lorem ipsum dolor sit amet,</text><text x="179" y="58" class="body-c">consectetuer adipiscing</text>
    <text x="265" y="47" class="label-c" style="fill:var(--orange)">Item 1</text><text x="265" y="53" class="body-c">Lorem ipsum dolor sit amet,</text><text x="265" y="58" class="body-c">consectetuer adipiscing</text>
    <text x="50" y="133" class="label-c">Item 1</text><text x="50" y="139" class="body-c">Lorem ipsum dolor sit amet,</text><text x="50" y="144" class="body-c">consectetuer adipiscing</text>
    <text x="136" y="133" class="label-c">Item 1</text><text x="136" y="139" class="body-c">Lorem ipsum dolor sit amet,</text><text x="136" y="144" class="body-c">consectetuer adipiscing</text>
    <text x="222" y="133" class="label-c">Item 1</text><text x="222" y="139" class="body-c">Lorem ipsum dolor sit amet,</text><text x="222" y="144" class="body-c">consectetuer adipiscing</text>
  </g>
  <use href="#foot"/>
</svg>

<!-- Row 4 -->
<svg class="slide c1 r4" viewBox="0 0 337 190">
  <text x="16" y="56" class="title-l">Doughnut Chart</text>
  <g transform="rotate(-90 160 82)" fill="none" stroke-width="14">
    <circle cx="160" cy="82" r="38" stroke="#d42129" stroke-dasharray="143 96"/>
    <circle cx="160" cy="82" r="38" stroke="#f59d34" stroke-dasharray="0 143 62 34"/>
    <circle cx="160" cy="82" r="38" stroke="#8a8a8a" stroke-dasharray="0 205 18 16"/>
    <circle cx="160" cy="82" r="38" stroke="#cfcfcf" stroke-dasharray="0 223 16 0"/>
  </g>
  <g class="body"><text x="122" y="142">● 1st Qtr   ● 2nd Qtr   ● 3rd Qtr   ● 4th Qtr</text></g>
  <text x="16" y="130" class="body">Lorem ipsum dolor sit amet,</text><text x="16" y="135" class="body">consectetuer adipiscing elit, sed</text><text x="16" y="140" class="body">diam nonummy nibh euismod</text>
  <text x="245" y="130" class="label" style="font-size:5px">Total</text>
  <text x="245" y="141" class="label" style="font-size:6px">13559</text>
  <use href="#foot"/>
</svg>

<svg class="slide c2 r4" viewBox="0 0 337 190">
  <rect width="337" height="75" fill="url(#amber)" role="img" aria-label="Photo: hand holding a bottle on a packing line"/>
  <text x="18" y="95" class="title-l">Product</text>
  <text x="18" y="105" class="body">Lorem ipsum dolor sit amet, consectetuer adipiscing elit,</text>
  <text x="18" y="110" class="body">sed diam nonummy nibh euismod tincidunt ut laoreet</text>
  <text x="18" y="115" class="body">dolore magna aliquam erat lorem ipsum dolor sit amet,</text>
  <text x="18" y="120" class="body">consectetuer adipiscing elit, sed diam nonummy nibh</text>
  <rect x="180" y="80" width="140" height="88" fill="url(#redAmber)" role="img" aria-label="Photo: bottle in an open gift box"/>
  <use href="#foot"/>
</svg>

<svg class="slide c3 r4" viewBox="0 0 337 190">
  <text x="16" y="26" class="title-l">Product</text>
  <g class="body">
    <text x="16" y="36">Lorem ipsum dolor sit amet, consectetuer adipiscing elit,</text>
    <text x="16" y="41">sed diam nonummy nibh euismod tincidunt ut laoreet</text>
    <text x="16" y="46">dolore magna aliquam erat lorem ipsum dolor sit amet,</text>
    <text x="16" y="51">consectetuer adipiscing elit, sed diam nonummy nibh</text>
    <text x="16" y="56">euismod tincidunt ut laoreet dolore magna aliquam erat</text>
    <text x="16" y="66">Lorem ipsum dolor sit amet, consectetuer adipiscing elit,</text>
    <text x="16" y="71">sed diam nonummy nibh euismod tincidunt ut laoreet</text>
    <text x="16" y="76">dolore magna aliquam erat lorem ipsum dolor sit amet,</text>
    <text x="16" y="81">consectetuer adipiscing elit, sed diam nonummy nibh</text>
    <text x="16" y="91">Lorem ipsum dolor sit amet, consectetuer adipiscing elit,</text>
    <text x="16" y="96">sed diam nonummy nibh euismod tincidunt ut laoreet</text>
  </g>
  <rect x="172" width="165" height="178" fill="url(#amber)" role="img" aria-label="Photo: decanter with gold stopper"/>
  <use href="#foot"/>
</svg>

<svg class="slide c4 r4" viewBox="0 0 337 190">
  <rect width="337" height="178" class="fill-orange"/>
  <text x="168" y="26" class="title" style="fill:#fff;font-weight:400">Infographic 03</text>
  <g class="fill-red">
    <rect x="16" y="58" width="60" height="100" rx="10"/><rect x="96" y="58" width="60" height="100" rx="10"/>
    <rect x="176" y="58" width="60" height="100" rx="10"/><rect x="256" y="58" width="60" height="100" rx="10"/>
  </g>
  <g fill="#fff" stroke="#d42129" stroke-width="2">
    <circle cx="46" cy="62" r="16"/><circle cx="126" cy="62" r="16"/><circle cx="206" cy="62" r="16"/><circle cx="286" cy="62" r="16"/>
  </g>
  <g class="num"><text x="46" y="63">500</text><text x="126" y="63">600</text><text x="206" y="63">700</text><text x="286" y="63">800</text></g>
  <g class="body-c" style="fill:var(--red)"><text x="46" y="69">Point A</text><text x="126" y="69">Point B</text><text x="206" y="69">Point C</text><text x="286" y="69">Point D</text></g>
  <g>
    <text x="22" y="92" class="label-w" style="font-size:3px">Step One</text><text x="22" y="99" class="body-w">Lorem ipsum dolor</text><text x="22" y="104" class="body-w">sit amet, consec</text>
    <text x="102" y="92" class="label-w" style="font-size:3px">Step Two</text><text x="102" y="99" class="body-w">Lorem ipsum dolor</text><text x="102" y="104" class="body-w">sit amet, consec</text>
    <text x="182" y="92" class="label-w" style="font-size:3px">Step Three</text><text x="182" y="99" class="body-w">Lorem ipsum dolor</text><text x="182" y="104" class="body-w">sit amet, consec</text>
    <text x="262" y="92" class="label-w" style="font-size:3px">Step Four</text><text x="262" y="99" class="body-w">Lorem ipsum dolor</text><text x="262" y="104" class="body-w">sit amet, consec</text>
  </g>
  <use href="#foot"/>
</svg>

<svg class="slide c5 r4" viewBox="0 0 337 190">
  <text x="168" y="26" class="title">Project Agenda</text>
  <text x="168" y="33" class="sub">Lorem ipsum dolor sit amet, consectetuer adipiscing elit.</text>
  <rect x="58" y="52" width="68" height="86" rx="3" fill="#fff" stroke="#e5e5e5"/>
  <rect x="135" y="52" width="68" height="86" rx="3" class="fill-orange"/>
  <rect x="212" y="52" width="68" height="86" rx="3" fill="#fff" stroke="#e5e5e5"/>
  <g class="icon" style="stroke-width:1.2">
    <circle cx="92" cy="75" r="4"/><path d="M90 80h4"/>
    <rect x="163" y="71" width="10" height="7" rx="1" stroke="#fff"/>
    <circle cx="243" cy="73" r="2.5"/><circle cx="250" cy="73" r="2.5"/><path d="M238 81a5 4 0 0 1 17 0"/>
  </g>
  <text x="92" y="97" class="label-c" style="font-size:3.5px">23rd June</text>
  <text x="169" y="97" class="label-c" style="font-size:3.5px;fill:#fff">14th July</text>
  <text x="246" y="97" class="label-c" style="font-size:3.5px">01st December</text>
  <g><text x="92" y="105" class="body-c">Lorem ipsum dolor sit amet,</text><text x="92" y="110" class="body-c">consectetuer adipiscing elit</text>
  <text x="169" y="105" class="body-c" style="fill:#fff">Lorem ipsum dolor sit amet,</text><text x="169" y="110" class="body-c" style="fill:#fff">consectetuer adipiscing elit</text>
  <text x="246" y="105" class="body-c">Lorem ipsum dolor sit amet,</text><text x="246" y="110" class="body-c">consectetuer adipiscing elit</text></g>
  <use href="#foot"/>
</svg>

<!-- Row 5 -->
<svg class="slide c1 r5" viewBox="0 0 337 190">
  <text x="168" y="26" class="title">Monthly Chart</text>
  <text x="168" y="33" class="sub">Lorem ipsum dolor sit amet, consectetuer adipiscing elit.</text>
  <g class="line-grey"><line x1="20" y1="52" x2="225" y2="52"/><line x1="20" y1="72" x2="225" y2="72"/><line x1="20" y1="92" x2="225" y2="92"/><line x1="20" y1="112" x2="225" y2="112"/><line x1="20" y1="132" x2="225" y2="132"/></g>
  <polyline points="38,72 72,92 108,82 140,70 175,86 210,58" class="line-red" stroke-width="1.2"/>
  <text x="250" y="54" class="label">May</text>
  <circle cx="258" cy="70" r="7" class="fill-red"/><text x="258" y="71.5" font-size="4" fill="#fff" text-anchor="middle" font-weight="700">3.5</text>
  <text x="250" y="85" class="body">Lorem ipsum dolor sit amet,</text><text x="250" y="90" class="body">consectetuer adipiscing elit</text>
  <text x="250" y="108" class="label">June</text>
  <circle cx="258" cy="124" r="7" class="fill-red"/><text x="258" y="125.5" font-size="4" fill="#fff" text-anchor="middle" font-weight="700">5.7</text>
  <text x="250" y="139" class="body">Lorem ipsum dolor sit amet,</text><text x="250" y="144" class="body">consectetuer adipiscing elit</text>
  <use href="#foot"/>
</svg>

<svg class="slide c2 r5" viewBox="0 0 337 190">
  <text x="168" y="26" class="title">Three Point Value</text>
  <text x="168" y="33" class="sub">Lorem ipsum dolor sit amet, consectetuer adipiscing elit.</text>
  <polyline points="62,92 150,134 232,78" fill="none" stroke="#8a8a8a" stroke-width="9" stroke-linecap="round"/>
  <g class="fill-red" stroke="#8a8a8a" stroke-width="2"><circle cx="62" cy="92" r="12"/><circle cx="150" cy="134" r="12"/><circle cx="232" cy="78" r="12"/></g>
  <g font-size="6" fill="#fff" font-weight="700" text-anchor="middle"><text x="62" y="94">1.</text><text x="150" y="136">2.</text><text x="232" y="80">3.</text></g>
  <text x="250" y="74" class="label">56%</text><text x="250" y="80" class="body">Lorem ipsum dolor sit amet, consectetuer</text>
  <text x="250" y="104" class="label">70%</text><text x="250" y="110" class="body">Lorem ipsum dolor sit amet, consectetuer</text>
  <text x="250" y="134" class="label">81%</text><text x="250" y="140" class="body">Lorem ipsum dolor sit amet, consectetuer</text>
  <use href="#foot"/>
</svg>

<svg class="slide c3 r5" viewBox="0 0 337 190">
  <rect width="337" height="190" class="fill-red"/>
  <text x="168" y="26" class="title" style="fill:#fff">Table</text>
  <text x="168" y="33" class="sub" style="fill:#fff">Lorem ipsum dolor sit amet, consectetuer adipiscing elit.</text>
  <rect x="48" y="50" width="242" height="9" class="fill-orange"/>
  <rect x="48" y="80" width="242" height="13" class="fill-orange"/>
  <rect x="48" y="122" width="242" height="13" class="fill-orange"/>
  <g class="body-w">
    <text x="51" y="56" font-weight="700">Data Name</text><text x="90" y="56" font-weight="700">Product</text><text x="130" y="56" font-weight="700">Profit</text><text x="175" y="56" font-weight="700">Optional</text><text x="210" y="56" font-weight="700">Sold</text><text x="255" y="56" font-weight="700">Performance</text>
    <text x="51" y="70">Data 1</text><text x="90" y="70">Product Name</text><text x="130" y="70">$900,000.00</text><text x="175" y="70">Yes</text><text x="210" y="70">70</text><text x="265" y="70">45%</text>
    <text x="51" y="88">Data 2</text><text x="90" y="88">Product Name</text><text x="130" y="88">$900,000.00</text><text x="175" y="88">No</text><text x="210" y="88">20</text><text x="265" y="88">20%</text>
    <text x="51" y="108">Data 3</text><text x="90" y="108">Product Name</text><text x="130" y="108">$900,000.00</text><text x="175" y="108">No</text><text x="210" y="108">20</text><text x="265" y="108">15%</text>
    <text x="51" y="130">Data 4</text><text x="90" y="130">Product Name</text><text x="130" y="130">$900,000.00</text><text x="175" y="130">Yes</text><text x="210" y="130">100</text><text x="265" y="130">60%</text>
    <text x="51" y="150">Data 5</text><text x="90" y="150">Product Name</text><text x="130" y="150">$900,000.00</text><text x="175" y="150">Yes</text><text x="210" y="150">50</text><text x="265" y="150">40%</text>
  </g>
  <use href="#foot"/>
</svg>

<svg class="slide c4 r5" viewBox="0 0 337 190">
  <text x="168" y="26" class="title">Dashboard 01</text>
  <rect x="185" y="42" width="48" height="22" class="fill-red"/>
  <text x="33" y="50" class="body-c">Customers</text><text x="33" y="58" class="label-c">2100</text>
  <text x="112" y="50" class="body-c">Profitably</text><text x="112" y="58" class="label-c">3100</text>
  <text x="209" y="50" class="body-c" style="fill:#fff">Projects</text><text x="209" y="58" class="label-c" style="fill:#fff">300</text>
  <text x="296" y="50" class="body-c">Returns</text><text x="296" y="58" class="label-c">14</text>
  <text x="33" y="78" class="label-c" style="font-size:3px">5 Active Users</text><text x="33" y="83" class="body-c">Last 10 Days</text>
  <text x="112" y="78" class="label-c" style="font-size:3px">2 Users per rate</text><text x="112" y="83" class="body-c">Last 10 Days</text>
  <g>
    <rect x="28" y="115" width="30" height="4" class="fill-red"/><rect x="58" y="115" width="14" height="4" class="fill-orange"/><rect x="72" y="115" width="20" height="4" class="fill-grey"/>
    <rect x="28" y="125" width="22" height="4" class="fill-red"/><rect x="50" y="125" width="18" height="4" class="fill-orange"/><rect x="68" y="125" width="12" height="4" class="fill-grey"/>
    <rect x="28" y="135" width="26" height="4" class="fill-red"/><rect x="54" y="135" width="16" height="4" class="fill-orange"/><rect x="70" y="135" width="14" height="4" class="fill-grey"/>
    <rect x="28" y="145" width="18" height="4" class="fill-red"/><rect x="46" y="145" width="22" height="4" class="fill-orange"/><rect x="68" y="145" width="10" height="4" class="fill-grey"/>
  </g>
  <g transform="rotate(-90 160 131)" fill="none" stroke-width="6">
    <circle cx="160" cy="131" r="20" stroke="#d42129" stroke-dasharray="80 46"/>
    <circle cx="160" cy="131" r="20" stroke="#f59d34" stroke-dasharray="0 80 40 6"/>
  </g>
  <text x="230" y="116" class="label" style="font-size:3.4px">Live Profit &amp; Net Sales</text>
  <text x="230" y="123" class="body" style="fill:var(--red)">Net Profit</text>
  <text x="230" y="130" class="label" style="font-size:3.4px">$55.432M</text>
  <text x="230" y="137" class="body" style="fill:var(--red)">Sales = 400,000</text>
  <use href="#foot"/>
</svg>

<svg class="slide c5 r5" viewBox="0 0 337 190">
  <text x="168" y="26" class="title">Dashboard 02</text>
  <text x="18" y="40" class="label" style="font-size:2.8px">Chart Title</text>
  <line x1="28" y1="44" x2="28" y2="96" class="line-grey"/><line x1="28" y1="96" x2="222" y2="96" class="line-grey"/>
  <g class="fill-red">
    <rect x="36" y="50" width="5" height="46"/><rect x="55" y="50" width="5" height="46"/><rect x="74" y="50" width="5" height="46"/><rect x="93" y="50" width="5" height="46"/>
    <rect x="112" y="50" width="5" height="46"/><rect x="131" y="50" width="5" height="46"/><rect x="150" y="50" width="5" height="46"/><rect x="169" y="50" width="5" height="46"/><rect x="188" y="50" width="5" height="46"/>
  </g>
  <circle cx="280" cy="72" r="18" class="fill-red"/>
  <path d="M280 72 L280 54 A18 18 0 0 0 263 66Z" class="fill-grey"/>
  <path d="M280 72 L263 66 A18 18 0 0 0 264 80Z" class="fill-orange"/>
  <g>
    <rect x="20" y="128" width="60" height="36" fill="#fafafa"/><path d="M20 164 L20 150 L40 138 L60 146 L80 128 L80 164Z" class="fill-orange"/><path d="M20 164 L20 156 L45 148 L80 140 L80 164Z" class="fill-red"/>
    <rect x="98" y="128" width="60" height="36" fill="#fafafa"/><path d="M98 164 L98 150 L118 138 L138 146 L158 128 L158 164Z" class="fill-orange"/><path d="M98 164 L98 156 L123 148 L158 140 L158 164Z" class="fill-red"/>
    <rect x="176" y="128" width="60" height="36" fill="#fafafa"/><path d="M176 164 L176 150 L196 138 L216 146 L236 128 L236 164Z" class="fill-orange"/><path d="M176 164 L176 156 L201 148 L236 140 L236 164Z" class="fill-red"/>
    <rect x="254" y="128" width="60" height="36" fill="#fafafa"/><path d="M254 164 L254 150 L274 138 L294 146 L314 128 L314 164Z" class="fill-orange"/><path d="M254 164 L254 156 L279 148 L314 140 L314 164Z" class="fill-red"/>
  </g>
  <use href="#foot"/>
</svg>

<!-- Row 6 -->
<svg class="slide c1 r6" viewBox="0 0 337 190">
  <text x="168" y="26" class="title">Dashboard 03</text>
  <text x="95" y="40" class="label-c" style="font-size:3px">Chart Title</text>
  <g class="line-grey"><line x1="35" y1="46" x2="160" y2="46"/><line x1="35" y1="58" x2="160" y2="58"/><line x1="35" y1="70" x2="160" y2="70"/><line x1="35" y1="82" x2="160" y2="82"/></g>
  <polyline points="38,56 65,70 92,52 120,66 150,60" class="line-red" stroke-width="1"/>
  <polyline points="38,68 65,58 92,66 120,56 150,72" fill="none" stroke="#555" stroke-width=".8"/>
  <polyline points="38,62 65,64 92,72 120,70 150,52" fill="none" stroke="#f59d34" stroke-width=".8"/>
  <text x="255" y="44" class="label-c" style="font-size:3px">Chart Title</text>
  <g class="fill-red"><rect x="212" y="52" width="72" height="3"/><rect x="212" y="60" width="80" height="3"/><rect x="212" y="68" width="60" height="3"/><rect x="212" y="76" width="76" height="3"/></g>
  <text x="95" y="107" class="label-c" style="font-size:3px">Chart Title</text>
  <line x1="30" y1="112" x2="30" y2="160" class="line-grey"/><line x1="30" y1="160" x2="165" y2="160" class="line-grey"/>
  <g>
    <rect x="38" y="130" width="4" height="30" class="fill-grey"/><rect x="43" y="138" width="4" height="22" class="fill-orange"/><rect x="48" y="142" width="4" height="18" class="fill-red"/>
    <rect x="68" y="124" width="4" height="36" class="fill-grey"/><rect x="73" y="134" width="4" height="26" class="fill-orange"/><rect x="78" y="140" width="4" height="20" class="fill-red"/>
    <rect x="98" y="132" width="4" height="28" class="fill-grey"/><rect x="103" y="140" width="4" height="20" class="fill-orange"/><rect x="108" y="144" width="4" height="16" class="fill-red"/>
    <rect x="128" y="136" width="4" height="24" class="fill-grey"/><rect x="133" y="130" width="4" height="30" class="fill-orange"/><rect x="138" y="118" width="4" height="42" class="fill-red"/>
  </g>
  <circle cx="202" cy="126" r="8" fill="none" stroke="#d42129" stroke-width="1.4"/>
  <rect x="199" y="122" width="6" height="8" rx=".5" class="fill-red"/>
  <text x="216" y="129" font-size="8" font-weight="700" fill="#d42129">436.00</text>
  <text x="196" y="142" class="body">Lorem ipsum dolor sit amet, consectetuer</text>
  <text x="196" y="147" class="body">adipiscing elit, sed diam nonummy nibh</text>
  <use href="#foot"/>
</svg>

<svg class="slide c2 r6" viewBox="0 0 337 190">
  <text x="168" y="26" class="title">Dashboard 04</text>
  <text x="240" y="40" class="label-c" style="font-size:3px;display:none">.</text>
  <text x="240" y="40" class="label" style="font-size:3px;display:none">.</text>
  <text x="122" y="40" class="label-c" style="font-size:3px">Chart Title</text>
  <path d="M40 100 L40 58 L90 62 L130 56 L175 68 L220 52 L220 100Z" class="fill-grey"/>
  <path d="M40 100 L40 78 L90 82 L130 80 L175 86 L220 70 L220 100Z" class="fill-red"/>
  <rect x="240" y="52" width="34" height="14" class="fill-light"/>
  <rect x="240" y="72" width="34" height="14" class="fill-light"/>
  <rect x="240" y="92" width="34" height="14" class="fill-red"/>
  <text x="243" y="58" class="label" style="font-size:3px">250</text><text x="243" y="63" class="body">Sales</text>
  <text x="243" y="78" class="label" style="font-size:3px">46</text><text x="243" y="83" class="body">New Clients</text>
  <text x="243" y="98" class="label-w" style="font-size:3px">15</text><text x="243" y="103" class="body-w">Employees</text>
  <text x="122" y="124" class="label-c" style="font-size:3px">Chart Title</text>
  <g>
    <rect x="40" y="130" width="60" height="3" class="fill-red"/><rect x="100" y="130" width="50" height="3" class="fill-orange"/><rect x="150" y="130" width="56" height="3" class="fill-grey"/>
    <rect x="40" y="138" width="70" height="3" class="fill-red"/><rect x="110" y="138" width="40" height="3" class="fill-orange"/><rect x="150" y="138" width="46" height="3" class="fill-grey"/>
    <rect x="40" y="146" width="50" height="3" class="fill-red"/><rect x="90" y="146" width="60" height="3" class="fill-orange"/><rect x="150" y="146" width="50" height="3" class="fill-grey"/>
    <rect x="40" y="154" width="66" height="3" class="fill-red"/><rect x="106" y="154" width="44" height="3" class="fill-orange"/><rect x="150" y="154" width="54" height="3" class="fill-grey"/>
  </g>
  <text x="240" y="128" class="label" style="font-size:3px">Title</text>
  <text x="240" y="134" class="body">Lorem ipsum dolor sit amet,</text><text x="240" y="139" class="body">consectetuer adipiscing elit</text><text x="240" y="144" class="body">sed diam nonummy nibh</text>
  <use href="#foot"/>
</svg>

<svg class="slide c3 r6" viewBox="0 0 337 190">
  <rect width="337" height="190" class="fill-red"/>
  <text x="168" y="70" font-size="16" font-weight="300" fill="#fff" text-anchor="middle">THANK YOU</text>
  <text x="168" y="84" class="body-c" style="fill:#fff">Lorem ipsum dolor sit amet, consectetuer adipiscing elit, sed diam nonummy nibh</text>
  <text x="168" y="90" class="body-c" style="fill:#fff">euismod tincidunt ut laoreet dolore magna aliquam erat volutpat. Ut wisi enim ad</text>
  <text x="168" y="96" class="body-c" style="fill:#fff">minim veniam, quis nostrud exerci tation ullamcorper suscipit lobortis nisl ut aliquip</text>
  <use href="#foot"/>
</svg>

<svg class="slide c4 r6" viewBox="0 0 337 190">
  <g class="icon">
    <circle cx="40" cy="28" r="5"/>
    <rect x="96" y="22" width="10" height="12" rx="1"/>
    <circle cx="166" cy="28" r="6"/><path d="M160 28h12M166 22v12"/>
    <circle cx="232" cy="26" r="3"/><path d="M227 34h10"/>
    <rect x="290" y="24" width="12" height="9" rx="1"/>
    <circle cx="40" cy="62" r="5"/><path d="M40 59v3l2 2"/>
    <path d="M96 58l10 10M106 58l-10 10"/>
    <rect x="160" y="57" width="12" height="8" rx="2"/>
    <circle cx="232" cy="62" r="3"/><path d="M232 55v2M232 67v2M225 62h2M237 62h2"/>
    <path d="M290 59l8-3v12l-8-3z"/>
    <circle cx="40" cy="95" r="5"/><circle cx="40" cy="95" r="2"/>
    <circle cx="101" cy="93" r="3"/><path d="M99 99h4"/>
    <circle cx="163" cy="93" r="2.5"/><circle cx="170" cy="93" r="2.5"/><path d="M159 100a5 4 0 0 1 14 0"/>
    <circle cx="232" cy="95" r="5"/>
    <path d="M290 98a6 4 0 0 1 12 0"/>
    <path d="M35 133v-5M39 133v-8M43 133v-11"/>
    <rect x="96" y="121" width="10" height="12" rx="1"/><path d="M98 125h6M98 128h6"/>
    <path d="M166 120l6 2v5c0 4-6 6-6 6s-6-2-6-6v-5z"/>
    <circle cx="229" cy="125" r="2.5"/><circle cx="236" cy="125" r="2.5"/><path d="M225 132a5 4 0 0 1 14 0"/>
    <circle cx="296" cy="127" r="5"/><circle cx="296" cy="127" r="1.8"/>
    <path d="M36 156v8h8v-5z"/>
    <path d="M101 154l6 3v6l-6 3-6-3v-6z"/>
    <path d="M166 166s-5-5-5-9a5 5 0 0 1 10 0c0 4-5 9-5 9z"/>
    <rect x="226" y="156" width="12" height="8" rx="1"/><path d="M226 156l6 5 6-5"/>
    <circle cx="296" cy="157" r="3"/><rect x="292" y="160" width="8" height="5" rx="1"/>
  </g>
  <use href="#foot"/>
</svg>

</body>
</html>
```